Australian Legal Practice would like a Web Design

I need a web design for a newly established law practice operating as Corvin Legal.

I would like the business to have an internet presence (via a website) essentially for the purpose of marketing and advertising. As the business grows (hopefully) I may be interested in providing general legal information as a means of establishing goodwill in the community and a easy and user friends contact method through the website.

The essence of the business is personal legal service based on local knowledge and therefore i want the website to present a picture of friendly professionalism, but mostly i want people who to be able to find the contact details of the business

I would like to have a map of the office location, and photos of the front of the office, the staff (me at the moment) and picture of law themed items and featuring the Corvin Legal logo.

The areas of law which Corvin Legal practises in are as follows:

commercial law
business sale and purchases
leases
conveyancing and property law
wills and estates
powers of attorney
general legal advice
succession planning

Reason: I have not had the opportunity to properly assess the designs and provide constructive feedback. I apologise for the inconvenience caused by my delay in providing feedback. Rob K.

Target Market(s)

Potential and existing clients of the firm
Other law firms
Associated stakeholders, i.e. Banks and real estate agents

Industry/Entity Type

Law Firm

Coding

Coded - Design and coding required

Number of Pages Required

2 page

Font styles to use
Sans Serif

Colors
85acd3
33a6d7
0456a4

Requirements
Must have
• Corvin Legal logo
• Map of the office location
• Picture of Rob Corvin (principal solicitor)
• Picture of the office
• Areas of Practice
• Address of office
• email address: rob.corvin@corvinlegal-example.com.au
• Physical address: 17 Ferncliff Road, Hamilton VIC 3300
• Phone number: (03) 5683 4917
• Facsimile number: (03) 5683 4038
• Space for a brief description of the firm and its competitive advantage
• Bar Guild Logo
• Links to the Bar Guild of Victoria
• Link to the practice standards Council
Nice to have
• coded to wordpress format

```html
<!DOCTYPE html>
<html lang="en">
<head>
<meta charset="utf-8">
<title>Corvin Legal</title>
<link rel="stylesheet" href="https://fonts.googleapis.com/css2?family=Open+Sans:wght@400;600;700&display=swap">
<style>
:root{
  --ink:#3d3d3d;
  --muted:#8a8a8a;
  --brand:#1d3f8f;
  --accent:#33a6d7;
  --line:#d9d9d9;
  --band:#ececec;
  --card:#f1f1f1;
  --footer:#4a4a4a;
  --footer-text:#c9c9c9;
  --base:#2c2c2c;
  --white:#ffffff;
}
*{margin:0;padding:0;box-sizing:border-box}
html,body{width:697px;height:1200px;overflow:hidden}
body{position:relative;background:var(--white);font-family:"Open Sans",Arial,sans-serif;color:var(--ink)}
.abs{position:absolute}

/* header */
.site-header{position:absolute;left:0;top:0;width:697px;height:72px;background:var(--white)}
.logo{left:100px;top:13px;display:flex;align-items:center;gap:6px;font-size:17px;font-weight:600;color:var(--brand);letter-spacing:.3px}
.logo-mark{width:10px;height:10px;background:var(--brand)}
.social{display:flex;gap:10px}
.social span{width:13px;height:13px;border-radius:50%;background:#b9b9b9}
.social .on{background:var(--accent)}
.header-social{left:508px;top:17px}
.main-nav{left:102px;top:50px;font-size:8px;color:#6b6b6b}
.main-nav a{position:absolute;white-space:nowrap;color:inherit;text-decoration:none}
.main-nav .current{color:var(--ink)}
.main-nav .current::after{content:"";position:absolute;left:-3px;right:-8px;top:18px;height:2px;background:var(--brand)}

/* hero */
.hero{left:0;top:72px;width:697px;height:232px;background:linear-gradient(100deg,#6b4a2d 0%,#9a6b40 35%,#b8845a 55%,#7a5433 80%,#4f3520 100%)}
.hero-title{left:0;width:697px;top:86px;text-align:center;color:var(--white);font-size:16px;font-weight:700;letter-spacing:.3px}
.hero-text{left:190px;width:340px;top:110px;text-align:center;color:#f3ebe3;font-size:7.5px;line-height:11px}
.hero-arrow{top:96px}
.hero-dots{left:318px;top:210px;display:flex;gap:5px}
.hero-dots span{width:8px;height:8px;border-radius:50%;border:1.5px solid var(--white)}
.hero-dots .active{background:var(--accent);box-shadow:inset 0 0 0 1.5px var(--white)}

/* intro */
.intro-title{left:0;width:697px;top:332px;text-align:center;font-size:12.5px;font-weight:400;color:#555}
.intro-title b{font-weight:700;color:#444}
.intro-text{left:100px;width:497px;top:355px;text-align:center;font-size:7.5px;line-height:13px;color:#9a9a9a}
.feature{width:160px;text-align:center}
.feature svg{display:block;margin:0 auto}
.feature h3{margin-top:8px;font-size:11px;font-weight:700;color:#666}
.feature p{margin:3px auto 0;width:154px;font-size:7px;line-height:10.5px;color:#999}

/* gallery */
.gallery-band{left:0;top:558px;width:697px;height:342px;background:var(--band)}
.gallery-notch{left:328px;top:534px}
.card{width:157px;height:143px;background:var(--card);border:1px solid var(--line)}
.card-photo{height:95px}
.card h4{margin:11px 10px 0;font-size:7.5px;font-weight:700;color:#555}
.card p{margin:3px 10px 0;font-size:7px;line-height:10px;color:#888}
.office-map{position:relative;background:#dfe7d6;overflow:hidden}

/* partners */
.partner{top:928px;font-size:18px;font-weight:600;color:#9c9c9c;transform:translateX(-50%);white-space:nowrap}

/* footer */
.site-footer{left:0;top:984px;width:697px;height:166px;background:var(--footer)}
.footer-col{top:1000px;width:110px;font-size:7px;line-height:9.5px;color:var(--footer-text)}
.footer-col h5{font-size:11.5px;font-weight:400;color:var(--white);margin-bottom:9px}
.footer-date{display:flex;align-items:center;gap:4px;margin-top:4px;color:#9a9a9a}
.footer-rule{height:1px;background:#5d5d5d;margin:8px 0}
.contact-row{display:flex;align-items:center;gap:7px;margin-top:5px;white-space:nowrap}
.contact-row svg{flex:none}
.base-bar{left:0;top:1150px;width:697px;height:50px;background:var(--base)}
.copyright{left:98px;top:1166px;font-size:7px;color:#bdbdbd}
.base-social{left:492px;top:1163px}
.base-social span{background:#9a9a9a}
</style>
</head>
<body>

<header class="site-header">
  <div class="abs logo"><span class="logo-mark"></span>Corvin Legal</div>
  <div class="abs social header-social"><span></span><span></span><span class="on"></span><span></span></div>
  <nav class="abs main-nav">
    <a class="current" style="left:0">Home</a>
    <a style="left:40px">About Us</a>
    <a style="left:92px">Leases</a>
    <a style="left:138px">Conveyancing</a>
    <a style="left:200px">Estate Planning</a>
    <a style="left:275px">Commercial</a>
    <a style="left:335px">Legal&nbsp; Service</a>
    <a style="left:406px">Fees-Contact</a>
  </nav>
</header>

<section class="abs hero" role="img" aria-label="Photo of brass scales of justice on a desk in a law library">
  <h1 class="abs hero-title">WELCOME TO CORVIN LEGAL</h1>
  <p class="abs hero-text">Lorem Ipsum is simply dummy text of the printing and typesetting industry. Lorem Ipsum has been the industry's standard dummy text ever since.</p>
  <svg class="abs hero-arrow" style="left:100px" width="12" height="24" viewBox="0 0 12 24"><path d="M11 1L1 12l10 11" fill="none" stroke="#fff" stroke-width="1.5"/></svg>
  <svg class="abs hero-arrow" style="left:585px" width="12" height="24" viewBox="0 0 12 24"><path d="M1 1l10 11L1 23" fill="none" stroke="#fff" stroke-width="1.5"/></svg>
  <div class="abs hero-dots"><span class="active"></span><span></span><span></span><span></span><span></span></div>
</section>

<h2 class="abs intro-title">LOREM IPSUM IS <b>SIMPLY DUMMY</b> OF THE PRINTING.</h2>
<p class="abs intro-text">Lorem Ipsum is simply dummy text of the printing and typesetting industry. Lorem Ipsum has been the industry's standard dummy text ever since the 1500s, when an unknown printer took a galley of type and scrambled it to make atype specimen book.<br>It has survived not only five centuries.</p>

<div class="abs feature" style="left:94px;top:413px">
  <svg width="42" height="42" viewBox="0 0 42 42" fill="none" stroke="#555" stroke-width="2.2">
    <path d="M6 17a16 16 0 0 1 27-8"/><path d="M33 3v7h-7"/>
    <path d="M36 25a16 16 0 0 1-27 8"/><path d="M9 39v-7h7"/>
    <circle cx="21" cy="16" r="4" fill="#555" stroke="none"/><path d="M13 30c1-6 4-8 8-8s7 2 8 8z" fill="#555" stroke="none"/>
  </svg>
  <h3>Lorem Ipsum</h3>
  <p>Lorem Ipsum is simply dummy text of the printing and typesetting of the industry.Lorem Ipsum has been</p>
</div>
<div class="abs feature" style="left:268px;top:413px">
  <svg width="50" height="42" viewBox="0 0 50 42" fill="#555">
    <circle cx="25" cy="15" r="5"/><path d="M15 31c0-7 4-10 10-10s10 3 10 10z"/>
    <circle cx="11" cy="17" r="4"/><path d="M3 31c0-6 3-9 8-9 2 0 4 1 5 2-2 2-3 4-3 7z"/>
    <circle cx="39" cy="17" r="4"/><path d="M47 31c0-6-3-9-8-9-2 0-4 1-5 2 2 2 3 4 3 7z"/>
  </svg>
  <h3>Lorem Ipsum</h3>
  <p>Lorem Ipsum is simply dummy text of the printing and typesetting of the industry.Lorem Ipsum has been</p>
</div>
<div class="abs feature" style="left:442px;top:413px">
  <svg width="42" height="42" viewBox="0 0 42 42" fill="none" stroke="#555" stroke-width="2.4">
    <path d="M28 8H8v26h26V18"/>
    <path d="M32 5l5 5-15 15-7 2 2-7z" fill="#555"/>
  </svg>
  <h3>Lorem Ipsum</h3>
  <p>Lorem Ipsum is simply dummy text of the printing and typesetting of the industry.Lorem Ipsum has been</p>
</div>

<div class="abs gallery-band"></div>
<svg class="abs gallery-notch" width="40" height="25" viewBox="0 0 40 25"><path d="M0 25L20 0l20 25z" fill="#ececec"/></svg>

<article class="abs card" style="left:98px;top:577px">
  <div class="card-photo" role="img" aria-label="Photo of a gavel and scales on a wooden desk" style="background:linear-gradient(135deg,#3e2418,#8a5a36 55%,#c59a6a)"></div>
  <h4>Lorem Ipsum is simply</h4><p>Lorem Ipsum is simply dummy text of the printing and typesetting of the</p>
</article>
<article class="abs card" style="left:270px;top:577px">
  <div class="card-photo" role="img" aria-label="Photo of a handshake over a signed document" style="background:linear-gradient(135deg,#1b1b1b,#4a4a4a 50%,#cfc8bd)"></div>
  <h4>Lorem Ipsum is simply</h4><p>Lorem Ipsum is simply dummy text of the printing and typesetting of the</p>
</article>
<article class="abs card" style="left:440px;top:577px">
  <div class="card-photo" role="img" aria-label="Photo of a gavel resting on a will and testament" style="background:linear-gradient(135deg,#d9c6a4,#8a4a22 55%,#3a1a0c)"></div>
  <h4>Lorem Ipsum is simply</h4><p>Lorem Ipsum is simply dummy text of the printing and typesetting of the</p>
</article>
<article class="abs card" style="left:98px;top:733px">
  <div class="card-photo" role="img" aria-label="Photo of principal solicitor Rob Corvin at the office" style="background:linear-gradient(180deg,#8d7d6c,#2a2a30 60%,#3a2a22)"></div>
  <h4>Lorem Ipsum is simply</h4><p>Lorem Ipsum is simply dummy text of the printing and typesetting of the</p>
</article>
<article class="abs card" style="left:270px;top:733px">
  <div class="card-photo" role="img" aria-label="Photo of the front of the Corvin Legal office" style="background:linear-gradient(135deg,#111,#5a4a38 45%,#d8c6a0)"></div>
  <h4>Lorem Ipsum is simply</h4><p>Lorem Ipsum is simply dummy text of the printing and typesetting of the</p>
</article>
<article class="abs card" style="left:440px;top:733px">
  <div class="card-photo office-map" role="img" aria-label="Map of the office location at 17 Ferncliff Road, Hamilton VIC 3300"></div>
  <h4>Find our office</h4><p>17 Ferncliff Road,<br>Hamilton VIC 3300</p>
</article>

<div class="abs partner" style="left:144px">stipplo</div>
<div class="abs partner" style="left:286px;font-size:13px;top:932px">lynxcat media</div>
<div class="abs partner" style="left:419px">Arcwork</div>
<div class="abs partner" style="left:554px">KESTREL</div>

<footer class="abs site-footer"></footer>
<div class="abs footer-col" style="left:98px">
  <h5>Populr Post</h5>
  <p>Lorem Ipsum is simply dummy text of the printing.</p>
  <div class="footer-date"><svg width="8" height="8" viewBox="0 0 8 8"><circle cx="4" cy="4" r="3.3" fill="none" stroke="#ccc"/><path d="M4 2v2h1.5" stroke="#ccc" fill="none"/></svg>25-September 2015</div>
  <div class="footer-rule"></div>
  <p>Lorem Ipsum is simply dummy text of the printing.</p>
  <div class="footer-date"><svg width="8" height="8" viewBox="0 0 8 8"><circle cx="4" cy="4" r="3.3" fill="none" stroke="#ccc"/><path d="M4 2v2h1.5" stroke="#ccc" fill="none"/></svg>25-September 2015</div>
</div>
<div class="abs footer-col" style="left:226px;width:120px">
  <h5>Areas of Practice</h5>
  <p>Commercial law<br>Business sale and purchases<br>Leases<br>Conveyancing and property law<br>Wills and estates<br>Powers of attorney<br>General legal advice<br>Succession planning</p>
</div>
<div class="abs footer-col" style="left:362px">
  <h5>A little about us</h5>
  <p>There are many variations of passages of Lorem Ipsum available, but the majority have suffered alteration in some form, by injected humour, or randomised words which don't look even</p>
</div>
<div class="abs footer-col" style="left:497px;width:145px">
  <h5>Get in touch</h5>
  <p style="width:112px">Lorem Ipsum is simply dummy of the printing and typesetting industry.</p>
  <div class="contact-row" style="margin-top:8px"><svg width="7" height="10" viewBox="0 0 7 10"><path d="M3.5 0A3.5 3.5 0 0 0 0 3.5C0 6 3.5 10 3.5 10S7 6 7 3.5A3.5 3.5 0 0 0 3.5 0z" fill="#fff"/><circle cx="3.5" cy="3.5" r="1.3" fill="#4a4a4a"/></svg>17 Ferncliff Road, Hamilton VIC 3300</div>
  <div class="contact-row"><svg width="8" height="8" viewBox="0 0 8 8"><path d="M1 0h2l1 2-1 1c.5 1 1 1.5 2 2l1-1 2 1v2C4 8 0 4 1 0z" fill="#fff"/></svg>Phone (03) 5683 4917</div>
  <div class="contact-row"><svg width="8" height="8" viewBox="0 0 8 8"><rect x="0" y="3" width="8" height="5" fill="#fff"/><rect x="2" y="0" width="4" height="3" fill="#fff"/></svg>Fax (03) 5683 4038</div>
  <div class="contact-row"><svg width="9" height="7" viewBox="0 0 9 7"><rect width="9" height="7" fill="#fff"/><path d="M0 0l4.5 4L9 0" stroke="#4a4a4a" fill="none"/></svg>rob.corvin@corvinlegal-example.com.au</div>
</div>

<div class="abs base-bar"></div>
<p class="abs copyright">© 2015 CORVIN LEGAL &nbsp;-&nbsp; All rights reserved</p>
<div class="abs social base-social"><span></span><span></span><span></span><span></span></div>

</body>
</html>
```